Bicycle Tour Schedule on a Business Card

Need to develop a 2 side business card that highlights a series of bike tours on 1 side and a series of events on the other side.
This will be inserted into a card wallet that attaches to a cell phone and will be handed out at an expo. The card wallets are black and red so color must coordinate with both. There is a photo of the card wallets attached.

1 side needs to be devoted to Pedal Vista Rides and the others to KRV Outcome events on the other. Dates and websites are very important.

Target Market(s)

Cyclists
Predominantly men ages 40+
Educated, Professionals

Industry/Entity Type

Business

Font styles to use
Serif

Requirements
Must have
• Pedal vista rides logo on 1 side and KRV Outcome logo on the other side
• dates and websites clearly visible
• Design of both sides must go together.
• Must be portrait not landscape

```html
<!DOCTYPE html>
<html lang="en">
<head>
<meta charset="utf-8">
<title>Pedal Vista Rides &amp; KRV Outcome – Event Cards</title>
<link rel="stylesheet" href="https://fonts.googleapis.com/css2?family=Open+Sans:wght@400;700;800&display=swap">
<style>
  :root {
    --backdrop: #e9e6e1;
    --paper: #ffffff;
    --tour-blue: #1f5fae;
    --tour-blue-text: #1b67b3;
    --tour-green: #39b54a;
    --event-red: #d41135;
    --event-line: #2a4f9e;
    --ink-grey: #6d6e71;
    --ink-dark: #58595b;
  }
  * { box-sizing: border-box; margin: 0; padding: 0; }
  html, body { width: 1200px; height: 950px; overflow: hidden; }
  body {
    background: var(--backdrop);
    font-family: "Open Sans", Arial, sans-serif;
    position: relative;
  }
  .card {
    position: absolute;
    top: 90px;
    width: 440px;
    height: 770px;
    background: var(--paper);
    box-shadow: 0 10px 28px rgba(0,0,0,0.18);
    overflow: hidden;
    text-align: center;
  }
  .card--tours { left: 130px; }
  .card--events { left: 630px; }

  .card__band {
    height: 250px;
    display: flex;
    align-items: center;
    justify-content: center;
    gap: 14px;
    position: relative;
  }
  .card--tours .card__band { background: var(--tour-blue); border-bottom: 5px solid var(--tour-green); }
  .card--events .card__band { background: var(--event-red); border-bottom: 4px solid var(--event-line); }

  .brand-mark {
    width: 26px; height: 26px;
    border-radius: 50%;
    background: #ffffff;
    flex: none;
  }
  .brand-name {
    color: #ffffff;
    font-weight: 800;
    font-size: 36px;
    letter-spacing: 0.5px;
    line-height: 1;
  }

  .card__body { padding: 34px 30px 0; }

  .tagline {
    color: var(--tour-blue-text);
    font-weight: 700;
    font-size: 27px;
    line-height: 1.2;
    margin-bottom: 24px;
  }
  .schedule { list-style: none; }
  .schedule li { line-height: 1.28; }
  .schedule .item-name { color: var(--ink-grey); font-size: 24px; font-weight: 400; display: block; }
  .schedule .item-date { color: var(--ink-dark); font-size: 24px; font-weight: 700; display: block; }

  .card--events .card__body { padding-top: 22px; }
  .event-group { margin-bottom: 12px; }
  .event-group:last-child { margin-bottom: 0; }
  .event-title {
    color: var(--event-red);
    font-weight: 700;
    font-size: 22px;
    line-height: 1.2;
  }
  .event-title--lead { font-size: 25px; margin-bottom: 2px; }
  .event-line { color: var(--ink-grey); font-size: 21px; line-height: 1.25; display: block; }
  .event-line--strong { color: var(--ink-dark); font-weight: 700; }
</style>
</head>
<body>

  <section class="card card--tours" aria-label="Pedal Vista Rides tour schedule">
    <header class="card__band">
      <span class="brand-mark" aria-hidden="true"></span>
      <span class="brand-name">PEDAL VISTA RIDES</span>
    </header>
    <div class="card__body">
      <p class="tagline">Fully supported bike tours. Discover the hidden gems on two wheels</p>
      <ul class="schedule">
        <li><span class="item-name">Heart of Colorado</span><span class="item-date">June 26 - July 2, 2016</span></li>
        <li><span class="item-name">Colorado Front Range Tour</span><span class="item-date">August 14-20, 2016</span></li>
        <li><span class="item-name">Cape Cod Tour</span><span class="item-date">October 9 -15, 2016</span></li>
        <li><span class="item-name">Florida Key Tours</span><span class="item-date">November 6-12, 2016 &amp;</span><span class="item-date">December 4-10, 2016</span></li>
      </ul>
    </div>
  </section>

  <section class="card card--events" aria-label="KRV Outcome event schedule">
    <header class="card__band">
      <span class="brand-mark" aria-hidden="true"></span>
      <span class="brand-name">KRV OUTCOME</span>
    </header>
    <div class="card__body">
      <div class="event-group">
        <h2 class="event-title event-title--lead">Trio Wheel Series:<br>Cycling camps for youth</h2>
        <span class="event-line">Mountain Bike Camp</span>
        <span class="event-line event-line--strong">July 8-10, 2016</span>
        <span class="event-line">Cyclocross Camp</span>
        <span class="event-line event-line--strong">August 26-28, 2016</span>
        <span class="event-line event-line--strong">Triowheelseries.org</span>
      </div>
      <div class="event-group">
        <h2 class="event-title">Mile High Hundred Ride</h2>
        <span class="event-line">June 18, 2016</span>
        <span class="event-line">Milehighhundred.com</span>
      </div>
      <div class="event-group">
        <h2 class="event-title">Summit Loop Challenge</h2>
        <span class="event-line">July 30, 2016</span>
        <span class="event-line">Summitloop.com</span>
      </div>
      <div class="event-group">
        <h2 class="event-title">Quirky Pedal Ride</h2>
        <span class="event-line">September 11, 2016</span>
        <span class="event-line">quirkypedal.com</span>
      </div>
    </div>
  </section>

</body>
</html>
```